Invest in Real Estate housing and apartment development projects in Lima - Peru

Need a presentation for Grupo Velmira, a top Real Estate developer from Peru who is looking for new leading investors such as Top Regional and Worldwide Real Estate funds and Regional Family offices and High Networth individuals to invest in Real Estate projects developed by/with Grupo Velmira. Velmira is focused on middle income apartments (housing) and has developed and delivered aprox 1400 apartments, and is currently developing and building 400 apartments. Velmira currently has a potential to develop 1500 more apartments. And is looking to raise between US $50 and 60mm dollars a year in additional new investments, all focused on real estate housing (essentially vertical housing, apartments)
I have already some information and slides prepared with information regarding management fees, development and sales/marketing fees, success fees which are alligned to IRR of the project.

Target Market(s)

Real Estate investors in Latin America

Industry/Entity Type

Real Estate Development

Colors

Designer to choose colors to be used in the design.

Requirements
Must have
• Graphs and pictures of real estate projects. Data of housing market from Lima, capital of Peru compared to other top capitals in South America

```html
<!DOCTYPE html>
<html lang="en">
<head>
<meta charset="utf-8">
<title>Grupo Velmira – Investor Presentation Templates</title>
<link href="https://fonts.googleapis.com/css2?family=Raleway:wght@300;400;600;700&family=Lato:wght@300;400;700&display=swap" rel="stylesheet">
<style>
:root{
  --green:#7cb642;
  --green-l:#9bcb5f;
  --green-d:#5e9a2c;
  --brown:#3d2b25;
  --brown-l:#5a453c;
  --grey:#9a9a9a;
  --grey-l:#d9d9d9;
  --paper:#ffffff;
  --ink:#3a3a3a;
  --sheet:#e8e8e8;
}
*{box-sizing:border-box}
html,body{margin:0;width:789px;height:1200px;overflow:hidden;background:var(--sheet);font-family:'Lato',sans-serif;color:var(--ink)}
.sheet{display:grid;grid-template-columns:repeat(3,257px);grid-auto-rows:145px;gap:5px;padding:2px 3px}
.slide{position:relative;background:var(--paper);overflow:hidden}
.abs{position:absolute}
.title{position:absolute;left:12px;top:7px;font-family:'Raleway',sans-serif;font-weight:400;font-size:11.5px;text-transform:uppercase;color:#333;letter-spacing:-.2px;white-space:nowrap}
.title.case{text-transform:none;font-size:12px}
.title::after{content:"";position:absolute;left:0;bottom:-4px;width:18px;height:1.5px;background:var(--green)}
.foot{position:absolute;left:6px;bottom:3px;display:flex;align-items:center;gap:3px;font-size:3.4px;color:#aaa}
.foot .brand{font-family:'Raleway',sans-serif;font-weight:700;font-size:5.5px;color:var(--brown);letter-spacing:.3px}
.foot .dot{width:5px;height:5px;border-radius:50%;background:var(--green)}
.tiny{font-size:3.4px;line-height:1.4;color:#999}
.lbl{font-size:4.2px;font-weight:700;color:#444}
.photo{position:absolute}
.ph-house{background:linear-gradient(160deg,#b7c7d6 0%,#8a7d70 45%,#4e6a3a 100%)}
.ph-city{background:linear-gradient(180deg,#6b5a50 0%,#4a3a33 60%,#2f2320 100%)}
.ph-night{background:linear-gradient(180deg,#3a3f57 0%,#7a5a46 55%,#2a2420 100%)}
.ph-skyline{background:linear-gradient(180deg,#f4f4f4 0%,#dedede 100%)}
.ph-map{background:linear-gradient(150deg,#d8d8d8,#c4c4c4)}
.avatar{position:absolute;border-radius:50%;background:linear-gradient(160deg,#d6dde3,#8c98a3)}
.divider-h{font-family:'Raleway',sans-serif;font-weight:700;color:#fff;font-size:13.5px;text-align:center;position:absolute;left:0;right:0}
.divider-s{position:absolute;right:40px;font-size:4.5px;color:#eee}
.logo-big{position:absolute;display:flex;align-items:center;gap:4px;font-family:'Raleway',sans-serif;font-weight:700;font-size:10px;letter-spacing:.5px}
.logo-big .dot{width:8px;height:8px;border-radius:50%;background:var(--green)}
.box{position:absolute;color:#fff;text-align:center;padding:4px 3px}
.box h4{margin:0 0 2px;font-size:4.3px;font-weight:700}
.box p{margin:0;font-size:3.2px;line-height:1.4;color:#f1f1f1}
.icon{position:absolute;border-radius:50%;display:flex;align-items:center;justify-content:center}
.item h5{margin:0;font-size:4.2px;font-weight:700;color:var(--green)}
.price{position:absolute;background:#fff;box-shadow:0 0 2px rgba(0,0,0,.2);text-align:center}
.price .head{color:#fff;font-family:'Raleway',sans-serif;font-size:11px;padding:3px 0 1px}
.price .head small{display:block;font-size:2.8px}
.price ul{list-style:none;margin:0;padding:0}
.price li{font-size:3px;color:#888;border-bottom:.5px solid #e5e5e5;padding:2.2px 0}
table.grid{position:absolute;left:12px;top:33px;width:233px;border-collapse:collapse;font-size:3.2px;color:#888}
table.grid th{background:var(--brown);color:#fff;font-weight:400;padding:1.3px}
table.grid td{text-align:center;padding:1.25px;border-bottom:.5px solid #e2e2e2}
table.grid td:first-child,table.grid th:first-child{text-align:left;padding-left:8px}
table.grid tr:first-child th:first-child{background:transparent;color:#555}
.member h5{margin:0;font-size:4.4px;color:#333;font-weight:700}
.member .role{font-size:3.2px;color:var(--green)}
</style>
</head>
<body>
<main class="sheet">

<section class="slide">
  <div class="photo ph-city" style="inset:0" role="img" aria-label="Aerial view of Lima residential district at dusk"></div>
  <div class="abs" style="inset:0;background:rgba(40,28,24,.45)"></div>
  <div class="divider-h" style="top:55px">THIS IS YOUR DIVIDER PAGE</div>
  <div class="divider-s" style="top:74px">Your Subtitle Goes Here</div>
  <div class="logo-big" style="right:8px;bottom:10px;color:#fff"><span class="dot"></span>Velmira</div>
</section>

<section class="slide">
  <div class="title">Quote Area</div>
  <div class="abs" style="left:0;top:22px;width:130px;height:114px;background:var(--green)"></div>
  <div class="abs" style="left:12px;top:40px;width:115px;color:#fff;font-size:6px;line-height:1.45;font-family:'Raleway',sans-serif">“Coming together is a beginning.<br>Keeping together is progress.<br>Working together is success.”<br><br>– Walter Brandt</div>
  <div class="photo ph-house" style="left:130px;top:22px;width:127px;height:114px" role="img" aria-label="Timber house with garden"></div>
  <div class="foot"><span class="dot"></span><span class="brand">Velmira</span> © Grupo Velmira. All rights reserved.</div>
</section>

<section class="slide">
  <div class="title">Brand Detailed</div>
  <div class="photo ph-house" style="left:18px;top:30px;width:118px;height:94px" role="img" aria-label="Two-storey white residence with tower"></div>
  <div class="box" style="left:138px;top:30px;width:47px;height:46px;background:var(--brown)"><h4>System</h4><p>Lorem ipsum dolor sit amet, porta luctus eget purus interdum.</p></div>
  <div class="box" style="left:187px;top:30px;width:47px;height:46px;background:var(--green)"><h4>Technology</h4><p>Lorem ipsum dolor sit amet, porta luctus eget purus interdum.</p></div>
  <div class="box" style="left:138px;top:78px;width:47px;height:46px;background:var(--green)"><h4>Leisure</h4><p>Lorem ipsum dolor sit amet, porta luctus eget purus interdum.</p></div>
  <div class="box" style="left:187px;top:78px;width:47px;height:46px;background:var(--brown)"><h4>Digital</h4><p>Lorem ipsum dolor sit amet, porta luctus eget purus interdum.</p></div>
  <div class="foot"><span class="dot"></span><span class="brand">Velmira</span> © Grupo Velmira. All rights reserved.</div>
</section>

<section class="slide">
  <div class="title">Product Philosophy</div>
  <svg class="abs" style="left:96px;top:44px" width="70" height="70" viewBox="0 0 70 70">
    <g fill="none" stroke-width="16" transform="rotate(-90 35 35)">
      <circle cx="35" cy="35" r="25" stroke="var(--brown)" stroke-dasharray="62.8 157"/>
      <circle cx="35" cy="35" r="25" stroke="var(--green-l)" stroke-dasharray="23.6 157" stroke-dashoffset="-62.8"/>
      <circle cx="35" cy="35" r="25" stroke="var(--green)" stroke-dasharray="39.3 157" stroke-dashoffset="-86.4"/>
      <circle cx="35" cy="35" r="25" stroke="var(--brown-l)" stroke-dasharray="31.4 157" stroke-dashoffset="-125.7"/>
    </g>
    <circle cx="35" cy="35" r="9" fill="var(--green)"/>
    <g font-size="5" font-weight="700" fill="#fff" font-family="Lato"><text x="48" y="18">15%</text><text x="52" y="40">25%</text><text x="27" y="64">20%</text><text x="4" y="32" fill="#222">40%</text></g>
  </svg>
  <div class="icon" style="left:78px;top:33px;width:16px;height:16px;background:var(--brown)"></div>
  <div class="abs" style="left:14px;top:33px;width:60px;text-align:right"><div class="lbl">Secure</div><div class="tiny">Nullam eu tempor purus nunc a leo magna sit amet.</div></div>
  <div class="icon" style="left:78px;top:100px;width:16px;height:16px;background:var(--brown)"></div>
  <div class="abs" style="left:14px;top:100px;width:60px;text-align:right"><div class="lbl">Good Package</div><div class="tiny">Nullam eu tempor purus nunc a leo magna sit amet.</div></div>
  <div class="icon" style="left:170px;top:33px;width:16px;height:16px;background:var(--green)"></div>
  <div class="abs item" style="left:190px;top:33px;width:56px"><h5>Well Organized</h5><div class="tiny">Nullam eu tempor purus nunc a leo magna sit amet.</div></div>
  <div class="icon" style="left:170px;top:100px;width:16px;height:16px;background:var(--green)"></div>
  <div class="abs item" style="left:190px;top:100px;width:56px"><h5>Publication</h5><div class="tiny">Nullam eu tempor purus nunc a leo magna sit amet.</div></div>
  <div class="foot"><span class="dot"></span><span class="brand">Velmira</span> © Grupo Velmira. All rights reserved.</div>
</section>

<section class="slide">
  <div class="photo ph-skyline" style="inset:0" role="img" aria-label="Faded city skyline"></div>
  <svg class="abs" style="left:0;top:0" width="257" height="145" viewBox="0 0 257 145">
    <g font-size="3.5" fill="#666"><circle cx="122" cy="24" r="1.3" fill="var(--green-d)"/><text x="125" y="25.3">2014</text><circle cx="137" cy="24" r="1.3" fill="var(--green-l)"/><text x="140" y="25.3">2015</text></g>
    <g fill="var(--green-d)"><rect x="28" y="66" width="14" height="44"/><rect x="86" y="74" width="14" height="36"/><rect x="144" y="78" width="14" height="32"/><rect x="200" y="80" width="14" height="30"/></g>
    <g fill="var(--green-l)"><rect x="44" y="54" width="14" height="56"/><rect x="102" y="44" width="14" height="66"/><rect x="160" y="84" width="14" height="26"/><rect x="216" y="96" width="14" height="14"/></g>
    <g font-size="4" fill="var(--green-d)" text-anchor="middle"><text x="35" y="64">400</text><text x="51" y="52">500</text><text x="93" y="72">300</text><text x="109" y="42">600</text><text x="151" y="76">250</text><text x="167" y="82">200</text><text x="207" y="78">200</text><text x="223" y="94">100</text></g>
    <rect x="0" y="110" width="257" height="35" fill="var(--brown)"/>
    <g font-size="4" fill="#fff" font-weight="700" text-anchor="middle"><text x="43" y="118">Asia</text><text x="101" y="118">Africa</text><text x="159" y="118">America</text><text x="215" y="118">Euro</text></g>
    <g font-size="3" fill="#cbbfb9" text-anchor="middle"><text x="43" y="124">Duis quis purus adipiscing mi</text><text x="101" y="124">Duis quis purus adipiscing mi</text><text x="159" y="124">Duis quis purus adipiscing mi</text><text x="215" y="124">Duis quis purus adipiscing mi</text></g>
  </svg>
</section>

<section class="slide">
  <div class="title">Trending in the World</div>
  <div class="photo ph-map" style="left:10px;top:30px;width:160px;height:92px;border-radius:6px" role="img" aria-label="World map silhouette"></div>
  <div class="icon" style="left:20px;top:72px;width:20px;height:20px;background:var(--brown);color:#fff;font-size:5.5px">25%</div>
  <div class="icon" style="left:74px;top:48px;width:32px;height:32px;background:var(--green-l);color:#fff;font-size:8px">80%</div>
  <div class="icon" style="left:112px;top:90px;width:16px;height:16px;background:var(--green);color:#fff;font-size:4.5px">15%</div>
  <div class="icon" style="left:138px;top:50px;width:28px;height:28px;background:var(--brown);color:#fff;font-size:7px">75%</div>
  <div class="icon" style="left:178px;top:38px;width:14px;height:14px;border:1px solid var(--brown)"></div>
  <div class="abs item" style="left:196px;top:38px;width:55px"><h5 style="color:#444">Confusion</h5><div class="tiny">Nullam eu tempor purus nunc sit amet.</div></div>
  <div class="icon" style="left:178px;top:66px;width:14px;height:14px;border:1px solid var(--green)"></div>
  <div class="abs item" style="left:196px;top:66px;width:55px"><h5>Intangible</h5><div class="tiny">Nullam eu tempor purus nunc sit amet.</div></div>
  <div class="icon" style="left:178px;top:94px;width:14px;height:14px;border:1px solid var(--green)"></div>
  <div class="abs item" style="left:196px;top:94px;width:55px"><h5>Performance</h5><div class="tiny">Nullam eu tempor purus nunc sit amet.</div></div>
  <div class="foot"><span class="dot"></span><span class="brand">Velmira</span> © Grupo Velmira. All rights reserved.</div>
</section>

<section class="slide">
  <div class="title">Peru Map</div>
  <div class="photo ph-map" style="left:22px;top:30px;width:70px;height:94px;border-radius:8px" role="img" aria-label="Map of Peru with Lima marked"></div>
  <svg class="abs" style="left:100px;top:48px" width="150" height="36" viewBox="0 0 150 36">
    <g fill="none" stroke-width="2.2">
      <circle cx="17" cy="18" r="14" stroke="#e3e3e3"/><circle cx="17" cy="18" r="14" stroke="var(--green-l)" stroke-dasharray="22 88" transform="rotate(-90 17 18)"/>
      <circle cx="55" cy="18" r="14" stroke="#e3e3e3"/><circle cx="55" cy="18" r="14" stroke="var(--brown)" stroke-dasharray="66 88" transform="rotate(-90 55 18)"/>
      <circle cx="93" cy="18" r="14" stroke="#e3e3e3"/><circle cx="93" cy="18" r="14" stroke="var(--brown)" stroke-dasharray="47 88" transform="rotate(-90 93 18)"/>
      <circle cx="131" cy="18" r="14" stroke="#e3e3e3"/><circle cx="131" cy="18" r="14" stroke="var(--green)" stroke-dasharray="79 88" transform="rotate(-90 131 18)"/>
    </g>
    <g font-size="7" text-anchor="middle" font-family="Raleway"><text x="17" y="20" fill="var(--green)">25%</text><text x="55" y="20" fill="var(--brown)">75%</text><text x="93" y="20" fill="var(--brown)">53%</text><text x="131" y="20" fill="var(--green)">90%</text></g>
  </svg>
  <div class="abs" style="left:108px;top:94px;background:var(--green);color:#fff;font-size:3.8px;padding:1px 3px">Fun Facts</div>
  <div class="abs tiny" style="left:108px;top:102px;width:140px;color:#555">Something project you should know. Lorem ipsum dolor sit amet, suitable for all categories <b>business</b> and <b>personal presentation</b>.</div>
  <div class="foot"><span class="dot"></span><span class="brand">Velmira</span> © Grupo Velmira. All rights reserved.</div>
</section>

<section class="slide">
  <div class="title">Population vs Housing in Peru</div>
  <div class="abs tiny" style="left:36px;top:43px;color:#444;font-size:3.8px">Population Data</div>
  <svg class="abs" style="left:36px;top:51px" width="125" height="18" viewBox="0 0 125 18">
    <g id="pp">
      <circle cx="5" cy="2.5" r="2.2"/><rect x="2" y="5.5" width="6" height="7" rx="1"/><rect x="2.6" y="12" width="2" height="6"/><rect x="5.4" y="12" width="2" height="6"/>
    </g>
    <g fill="var(--brown)"><use href="#pp"/><use href="#pp" x="12"/><use href="#pp" x="24"/><use href="#pp" x="36"/><use href="#pp" x="48"/><use href="#pp" x="60"/><use href="#pp" x="72"/><use href="#pp" x="84"/><use href="#pp" x="96"/></g>
    <use href="#pp" x="108" fill="#bbb"/>
  </svg>
  <div class="abs" style="left:170px;top:49px;font-family:'Raleway';font-size:12px;color:#333">15,2M</div>
  <div class="abs tiny" style="left:172px;top:65px;color:#555">Based on <b>2015</b>survey</div>
  <div class="abs tiny" style="left:36px;top:82px;color:#444;font-size:3.8px">House Data</div>
  <svg class="abs" style="left:36px;top:90px" width="125" height="14" viewBox="0 0 125 14">
    <g id="hh"><polygon points="0,6 5,1 10,6"/><rect x="1.5" y="6" width="7" height="8"/></g>
    <g fill="var(--green)"><use href="#hh"/><use href="#hh" x="12"/><use href="#hh" x="24"/><use href="#hh" x="36"/><use href="#hh" x="48"/><use href="#hh" x="60"/><use href="#hh" x="72"/><use href="#hh" x="84"/></g>
    <g fill="#bbb"><use href="#hh" x="96"/><use href="#hh" x="108"/></g>
  </svg>
  <div class="abs" style="left:170px;top:88px;font-family:'Raleway';font-size:12px;color:var(--green)">11,7M</div>
  <div class="abs tiny" style="left:172px;top:104px;color:#555">Based on <b>2015</b>survey</div>
  <div class="foot"><span class="dot"></span><span class="brand">Velmira</span> © Grupo Velmira. All rights reserved.</div>
</section>

<section class="slide">
  <div class="title">Our Vision &amp; Mission</div>
  <div class="photo" style="left:0;top:25px;width:257px;height:110px;background:linear-gradient(120deg,#4a3730,#3d2b25 60%,#2f211c)" role="img" aria-label="Apartment building facade in dark tone"></div>
  <div class="abs" style="left:12px;top:34px;width:115px;color:#fff">
    <div style="font-size:5.5px">• Our Vision:</div>
    <div style="font-size:4.8px;font-weight:700;margin:2px 0 3px">Go to the Next Level<br>Without look in the past</div>
    <div class="tiny" style="color:#cbbfb9">Lorem ipsum dolor sit amet consectetur adipiscing elit sed do eiusmod tempor incididunt ut labore et dolore magna aliqua ut enim ad minim veniam.</div>
  </div>
  <div class="abs" style="left:140px;top:34px;width:110px;color:#fff;font-size:5.5px">• Our Missions:</div>
  <div class="icon" style="left:147px;top:45px;width:10px;height:10px;background:#fff"></div>
  <div class="abs" style="left:161px;top:44px;width:90px"><div style="font-size:4.6px;color:var(--green-l)">Your Text Here</div><div class="tiny" style="color:#cbbfb9">Lorem ipsum dolor sit consectetur adipiscing elit sed do eiusmod.</div></div>
  <div class="icon" style="left:147px;top:66px;width:10px;height:10px;background:#fff"></div>
  <div class="abs" style="left:161px;top:65px;width:90px"><div style="font-size:4.6px;color:var(--green-l)">Your Text Here</div><div class="tiny" style="color:#cbbfb9">Lorem ipsum dolor sit consectetur adipiscing elit sed do eiusmod.</div></div>
  <div class="icon" style="left:147px;top:87px;width:10px;height:10px;background:#fff"></div>
  <div class="abs" style="left:161px;top:86px;width:90px"><div style="font-size:4.6px;color:var(--green-l)">Your Text Here</div><div class="tiny" style="color:#cbbfb9">Lorem ipsum dolor sit consectetur adipiscing elit sed do eiusmod.</div></div>
  <div class="foot"><span class="dot"></span><span class="brand">Velmira</span> © Grupo Velmira. All rights reserved.</div>
</section>

<section class="slide">
  <div class="title">Our Services</div>
  <div class="photo" style="left:24px;top:30px;width:100px;height:63px;background:linear-gradient(150deg,#5c7389,#26384a)" role="img" aria-label="Businessman with rising growth chart"></div>
  <div class="abs" style="left:24px;top:98px;font-size:4.6px;color:#444">Your Title Goes Here</div>
  <div class="abs tiny" style="left:24px;top:104px;width:100px">Lorem ipsum dolor sit amet consectetur adipiscing elit sed do eiusmod tempor incididunt ut labore et dolore magna aliqua.</div>
  <div class="icon" style="left:142px;top:34px;width:9px;height:9px;background:var(--brown)"></div>
  <div class="abs" style="left:157px;top:32px;width:92px"><div style="font-size:4.6px;color:#444">Service Number One</div><div class="tiny">Lorem ipsum dolor sit amet consectetur adipiscing elit sed do eiusmod tempor.</div></div>
  <div class="icon" style="left:142px;top:64px;width:9px;height:9px;background:var(--green)"></div>
  <div class="abs" style="left:157px;top:62px;width:92px"><div style="font-size:4.6px;color:var(--green)">Service Number Two</div><div class="tiny">Lorem ipsum dolor sit amet consectetur adipiscing elit sed do eiusmod tempor.</div></div>
  <div class="icon" style="left:142px;top:94px;width:9px;height:9px;background:var(--green)"></div>
  <div class="abs" style="left:157px;top:92px;width:92px"><div style="font-size:4.6px;color:var(--green)">Service Number Three</div><div class="tiny">Lorem ipsum dolor sit amet consectetur adipiscing elit sed do eiusmod tempor.</div></div>
  <div class="foot"><span class="dot"></span><span class="brand">Velmira</span> © Grupo Velmira. All rights reserved.</div>
</section>

<section class="slide">
  <div class="title">Three Column Description</div>
  <div class="abs" style="left:14px;top:36px;width:190px;font-size:5px;color:#333;line-height:1.3">This is place for your header text. Insert your text here, just replace this with your own text</div>
  <div class="abs tiny" style="left:14px;top:56px;width:70px">Lorem ipsum dolor sit amet, consectetur adipiscing elit sed do eiusmod tempor incididunt ut labore et dolore magna aliqua. Ut enim ad minim veniam, quis nostrud exercitation ullamco laboris nisi ut aliquip ex ea commodo consequat.<br><br>Duis aute irure dolor in reprehenderit in voluptate velit esse cillum dolore eu fugiat nulla pariatur.</div>
  <div class="abs tiny" style="left:93px;top:56px;width:70px">Lorem ipsum dolor sit amet, consectetur adipiscing elit sed do eiusmod tempor incididunt ut labore et dolore magna aliqua. Ut enim ad minim veniam, quis nostrud exercitation ullamco laboris nisi ut aliquip ex ea commodo consequat.<br><br>Duis aute irure dolor in reprehenderit in voluptate velit esse cillum dolore eu fugiat nulla pariatur.</div>
  <div class="abs tiny" style="left:172px;top:56px;width:70px">Lorem ipsum dolor sit amet, consectetur adipiscing elit sed do eiusmod tempor incididunt ut labore et dolore magna aliqua. Ut enim ad minim veniam, quis nostrud exercitation ullamco.<br><br>Duis aute irure dolor in reprehenderit in voluptate velit esse cillum dolore eu fugiat nulla pariatur.</div>
  <div class="foot"><span class="dot"></span><span class="brand">Velmira</span> © Grupo Velmira. All rights reserved.</div>
</section>

<section class="slide">
  <div class="title">Our Team</div>
  <div class="avatar" style="left:97px;top:31px;width:62px;height:62px" role="img" aria-label="Portrait of team member"></div>
  <div class="abs" style="left:0;right:0;top:98px;text-align:center;font-size:4px;color:#444">Mr. John Smith</div>
  <div class="abs" style="left:0;right:0;top:103px;text-align:center;font-size:3.4px;color:var(--green)">CEO</div>
  <div class="abs tiny" style="left:70px;top:108px;width:117px;text-align:center">Lorem ipsum dolor sit amet consectetur adipiscing elit sed do eiusmod tempor incididunt.</div>
  <div class="abs" style="left:113px;top:123px;display:flex;gap:2px"><span style="width:4px;height:4px;border-radius:50%;background:#333"></span><span style="width:4px;height:4px;border-radius:50%;background:#333"></span><span style="width:4px;height:4px;border-radius:50%;background:#333"></span><span style="width:4px;height:4px;border-radius:50%;background:#333"></span><span style="width:4px;height:4px;border-radius:50%;background:#333"></span></div>
  <div class="foot"><span class="dot"></span><span class="brand">Velmira</span> © Grupo Velmira. All rights reserved.</div>
</section>

<section class="slide">
  <div class="photo" style="inset:0;background:linear-gradient(180deg,#8cc152 0%,#76b03f 60%,#5e8f32 100%)" role="img" aria-label="Lima cityscape washed in green"></div>
  <svg class="abs" style="left:0;top:0" width="60" height="40" viewBox="0 0 60 40"><polygon points="0,0 60,0 0,40" fill="#fff"/></svg>
  <div class="logo-big" style="left:8px;top:10px;color:var(--brown)"><span class="dot"></span>Velmira</div>
  <div class="divider-h" style="top:67px">THIS IS YOUR DIVIDER PAGE</div>
  <div class="divider-s" style="top:86px">Your Subtitle Goes Here</div>
</section>

<section class="slide">
  <div class="title">Monthly Subscription</div>
  <div class="abs" style="left:0;top:50px;width:257px;height:60px;background:var(--brown)"></div>
  <div class="price" style="left:38px;top:48px;width:50px;height:70px"><div class="head" style="background:#4d3a33">$300<small>per month</small></div><ul><li>Single Edition</li><li>High Cloud Service</li><li>3 User</li><li>Free Update</li></ul></div>
  <div class="price" style="left:104px;top:44px;width:52px;height:82px"><div class="head" style="background:var(--green);padding:5px 0 3px">$900<small>per month</small></div><ul><li>Business Edition</li><li>High Cloud Service</li><li>5 User</li><li>Free Update</li></ul></div>
  <div class="price" style="left:172px;top:48px;width:50px;height:70px"><div class="head" style="background:var(--green)">$400<small>per month</small></div><ul><li>Single Edition</li><li>High Cloud Service</li><li>3 User</li><li>Free Update</li></ul></div>
</section>

<section class="slide">
  <div class="title">Your Title Goes Here</div>
  <div class="abs tiny" style="left:12px;top:24px;width:230px">Description · Lorem ipsum dolor sit amet consectetur adipiscing elit sed do eiusmod</div>
  <table class="grid">
    <tr><th></th><th>Value</th><th>Value</th><th>Value</th><th>Value</th></tr>
    <tr><td>Lorem ipsum</td><td>10</td><td>15</td><td>16</td><td>18</td></tr>
    <tr><td>Lorem ipsum</td><td>12</td><td>11</td><td>15</td><td>16</td></tr>
    <tr><td>Lorem ipsum</td><td>20</td><td>22</td><td>25</td><td>21</td></tr>
    <tr><td>Lorem ipsum</td><td>10</td><td>25</td><td>12</td><td>15</td></tr>
    <tr><td>Lorem ipsum</td><td>25</td><td>25</td><td>25</td><td>25</td></tr>
    <tr><td>Lorem ipsum</td><td>10</td><td>02</td><td>52</td><td>21</td></tr>
    <tr><td>Lorem ipsum</td><td>25</td><td>32</td><td>65</td><td>52</td></tr>
    <tr><td>Lorem ipsum</td><td>26</td><td>35</td><td>26</td><td>32</td></tr>
    <tr><td>Lorem ipsum</td><td>32</td><td>18</td><td>30</td><td>30</td></tr>
  </table>
  <div class="foot"><span class="dot"></span><span class="brand">Velmira</span> © Grupo Velmira. All rights reserved.</div>
</section>

<section class="slide">
  <div class="title">Our Team</div>
  <div class="avatar" style="left:18px;top:38px;width:20px;height:20px" role="img" aria-label="Portrait of team member"></div>
  <div class="abs member" style="left:48px;top:40px;width:76px"><h5>Michael Doe</h5><div class="role">CEO</div><div class="tiny">• Lorem ipsum dolor sit amet consectetur<br>• Sed do eiusmod tempor incididunt</div></div>
  <div class="avatar" style="left:138px;top:38px;width:20px;height:20px" role="img" aria-label="Portrait of team member"></div>
  <div class="abs member" style="left:166px;top:40px;width:80px"><h5>James Doe</h5><div class="role">Manager</div><div class="tiny">• Lorem ipsum dolor sit amet consectetur<br>• Sed do eiusmod tempor incididunt</div></div>
  <div class="avatar" style="left:18px;top:86px;width:20px;height:20px" role="img" aria-label="Portrait of team member"></div>
  <div class="abs member" style="left:48px;top:88px;width:76px"><h5>Jane Doe</h5><div class="role">Doctor of Chemistry</div><div class="tiny">• Lorem ipsum dolor sit amet consectetur<br>• Sed do eiusmod tempor incididunt</div></div>
  <div class="avatar" style="left:138px;top:86px;width:20px;height:20px" role="img" aria-label="Portrait of team member"></div>
  <div class="abs member" style="left:166px;top:88px;width:80px"><h5>John Doe</h5><div class="role">Professor</div><div class="tiny">• Lorem ipsum dolor sit amet consectetur<br>• Sed do eiusmod tempor incididunt</div></div>
  <div class="foot"><span class="dot"></span><span class="brand">Velmira</span> © Grupo Velmira. All rights reserved.</div>
</section>

<section class="slide">
  <div class="title">Customer Testimonials</div>
  <div class="avatar" style="left:56px;top:32px;width:32px;height:32px" role="img" aria-label="Portrait of client"></div>
  <div class="abs tiny" style="left:108px;top:36px;width:120px">Adipiscing elit sed diam nonummy nibh euismod tincidunt ut laoreet dolore magna aliquam erat volutpat. Ut wisi enim ad minim veniam, quis nostrud exerci tation ullamcorper suscipit lobortis nisl ut aliquip.</div>
  <div class="abs" style="left:0;top:72px;width:257px;height:73px;background:var(--green)"></div>
  <svg class="abs" style="left:0;top:72px" width="257" height="73" viewBox="0 0 257 73">
    <g fill="none" stroke="#fff" stroke-width=".8"><circle cx="42" cy="24" r="8"/><circle cx="107" cy="24" r="8"/><circle cx="172" cy="24" r="8"/><circle cx="237" cy="24" r="8"/>
    <rect x="38" y="21" width="8" height="6"/><rect x="103" y="21" width="8" height="6"/><rect x="168" y="21" width="8" height="6"/><rect x="233" y="21" width="8" height="6"/></g>
    <g font-size="3" fill="#eaf5dd" text-anchor="middle"><text x="42" y="42">Why does getting a loan</text><text x="42" y="46">have to be so hard?</text><text x="107" y="42">Who do I have to go to</text><text x="107" y="46">for a home loan?</text><text x="172" y="42">Why do banks refuse</text><text x="172" y="46">to lend to me?</text><text x="237" y="42">Why is there no</text><text x="237" y="46">easy application?</text></g>
  </svg>
</section>

<section class="slide">
  <div class="title">Two Pictures Slide</div>
  <div class="photo ph-house" style="left:22px;top:30px;width:106px;height:97px" role="img" aria-label="Stone family house with garage"></div>
  <div class="photo ph-house" style="left:132px;top:30px;width:106px;height:97px;background:linear-gradient(160deg,#c6d3de,#9a8574 50%,#5a7a40)" role="img" aria-label="Two-storey brick home with lawn"></div>
  <div class="foot"><span class="dot"></span><span class="brand">Velmira</span> © Grupo Velmira. All rights reserved.</div>
</section>

<section class="slide">
  <div class="title">Title and Image + Text</div>
  <div class="photo ph-night" style="left:20px;top:28px;width:218px;height:54px" role="img" aria-label="Modern apartment complex at dusk"></div>
  <div class="abs" style="left:20px;top:88px;width:105px;font-size:5.4px;line-height:1.3;color:#444">Lorem ipsum dolor sit amet, consectetur adipiscing elit, sed do eiusmod tempor incididunt ut labore et dolore magna aliqua. Ut enim ad minim veniam, quis</div>
  <div class="abs tiny" style="left:134px;top:88px;width:104px">Lorem ipsum dolor sit amet, consectetur adipiscing elit sed do eiusmod tempor incididunt ut labore et dolore magna aliqua.<br><br>Duis aute irure dolor in reprehenderit in voluptate velit esse cillum dolore eu fugiat nulla pariatur excepteur sint.</div>
  <div class="foot"><span class="dot"></span><span class="brand">Velmira</span> © Grupo Velmira. All rights reserved.</div>
</section>

<section class="slide">
  <div class="title case">Home Improvements</div>
  <svg class="abs" style="left:12px;top:28px" width="110" height="110" viewBox="0 0 110 110">
    <g stroke="#e3e3e3" stroke-width=".5"><line x1="6" y1="10" x2="100" y2="10"/><line x1="6" y1="30" x2="100" y2="30"/><line x1="6" y1="50" x2="100" y2="50"/><line x1="6" y1="70" x2="100" y2="70"/></g>
    <rect x="20" y="46" width="14" height="30" fill="var(--brown)"/><rect x="34" y="20" width="14" height="56" fill="var(--green)"/><rect x="48" y="60" width="14" height="16" fill="var(--green-l)"/><rect x="62" y="52" width="14" height="24" fill="var(--green)"/>
    <rect x="32" y="8" width="16" height="8" fill="var(--green-l)"/><text x="40" y="14" font-size="4" fill="#fff" text-anchor="middle">50%</text>
    <line x1="6" y1="76" x2="100" y2="76" stroke="#999" stroke-width=".5"/>
    <g font-size="3.2" fill="#333">
      <circle cx="6" cy="92" r="2.5" fill="var(--brown)"/><text x="10" y="93">Description</text>
      <circle cx="36" cy="92" r="2.5" fill="var(--green)"/><text x="40" y="93">Description</text>
      <circle cx="66" cy="92" r="2.5" fill="var(--green)"/><text x="70" y="93">Description</text>
      <circle cx="20" cy="103" r="2.5" fill="var(--brown)"/><text x="24" y="104">Description</text>
      <circle cx="50" cy="103" r="2.5" fill="var(--green)"/><text x="54" y="104">Description</text>
    </g>
  </svg>
  <div class="photo" style="left:128px;top:28px;width:120px;height:110px;background:linear-gradient(170deg,#6b5a48 0%,#6f9a45 55%,#7cb642 100%)" role="img" aria-label="Cutaway illustration of house interior rooms"></div>
  <div class="foot"><span class="dot"></span><span class="brand">Velmira</span> © Grupo Velmira. All rights reserved.</div>
</section>

<section class="slide">
  <div class="title case">Building Infographic</div>
  <div class="photo ph-skyline" style="left:0;top:30px;width:257px;height:85px" role="img" aria-label="Faded city skyline background"></div>
  <svg class="abs" style="left:0;top:30px" width="257" height="115" viewBox="0 0 257 115">
    <g stroke="#ddd" stroke-width=".5"><line x1="25" y1="8" x2="250" y2="8"/><line x1="25" y1="30" x2="250" y2="30"/><line x1="25" y1="52" x2="250" y2="52"/></g>
    <g font-size="3" fill="#999"><text x="10" y="9">100%</text><text x="12" y="31">75%</text><text x="12" y="53">50%</text></g>
    <g fill="var(--brown)"><rect x="50" y="60" width="14" height="25"/><rect x="135" y="40" width="14" height="45"/><rect x="220" y="60" width="14" height="25"/></g>
    <g fill="var(--green)"><rect x="92" y="58" width="14" height="27"/><rect x="178" y="50" width="14" height="35"/><rect x="245" y="45" width="10" height="40"/></g>
    <g fill="var(--green-l)"><rect x="70" y="68" width="12" height="17"/><rect x="113" y="62" width="12" height="23"/><rect x="156" y="64" width="12" height="21"/><rect x="198" y="66" width="12" height="19"/></g>
    <rect x="0" y="85" width="257" height="30" fill="var(--brown)"/>
    <g font-size="3.5" fill="#fff" text-anchor="middle" font-weight="700"><text x="57" y="91">2011</text><text x="99" y="91">2012</text><text x="142" y="91">2013</text><text x="185" y="91">2014</text><text x="227" y="91">2015</text></g>
    <g font-size="3" fill="#d8cdc7" text-anchor="middle"><text x="128" y="100">Contrary to popular belief, Lorem Ipsum is not simply random text. It has roots in a piece of classical Latin literature.</text><text x="128" y="105">Contrary to popular belief, it has roots in classical Latin literature from 45 BC.</text></g>
  </svg>
</section>

<section class="slide">
  <div class="title case">Property Infographic</div>
  <div class="photo" style="left:12px;top:44px;width:112px;height:70px;background:linear-gradient(120deg,#a5a5a5 0%,#6b5a50 50%,#7cb642 100%)" role="img" aria-label="Key illustration with labels House, Rent, Penthouse, Sale"></div>
  <div class="abs" style="left:140px;top:60px;font-size:5px;color:var(--green)">Description</div>
  <div class="abs" style="left:140px;top:67px;font-family:'Raleway';font-size:12px;font-weight:600;color:#333">35%</div>
  <div class="abs tiny" style="left:164px;top:67px;width:82px">Of shopping costs are abandoned right before the transaction is completed.</div>
  <div class="abs tiny" style="left:140px;top:84px;width:106px">For every 6 emails received we get 1 phone calls. Suitable for all categories business and personal presentation, eaque ipsa quae ab illo inventore veritatis et quasi.</div>
  <div class="foot"><span class="dot"></span><span class="brand">Velmira</span> © Grupo Velmira. All rights reserved.</div>
</section>

<section class="slide">
  <div class="title case">House Infographic</div>
  <div class="photo" style="left:0;top:30px;width:257px;height:90px;background:linear-gradient(180deg,#efefef,#cfcfcf)" role="img" aria-label="Grey city silhouette"></div>
  <svg class="abs" style="left:0;top:30px" width="257" height="115" viewBox="0 0 257 115">
    <g fill="var(--green)"><rect x="100" y="48" width="24" height="45"/><rect x="182" y="28" width="24" height="65"/><rect x="220" y="20" width="24" height="73"/></g>
    <g fill="var(--brown)"><rect x="140" y="40" width="24" height="53"/></g>
    <g fill="var(--green-l)"><rect x="60" y="58" width="24" height="35"/></g>
    <g font-size="4.5" fill="#fff" text-anchor="middle"><text x="72" y="72">+20%</text><text x="112" y="62">+35%</text><text x="152" y="54">+30%</text><text x="194" y="42">+40%</text><text x="232" y="34">+50%</text></g>
    <rect x="0" y="93" width="257" height="22" fill="var(--brown)"/>
    <g fill="var(--green-d)"><circle cx="72" cy="93" r="5"/><circle cx="112" cy="93" r="5"/><circle cx="152" cy="93" r="5"/><circle cx="194" cy="93" r="5"/><circle cx="232" cy="93" r="5"/></g>
    <g font-size="3" fill="#fff" text-anchor="middle"><text x="72" y="94">2011</text><text x="112" y="94">2012</text><text x="152" y="94">2013</text><text x="194" y="94">2014</text><text x="232" y="94">2015</text></g>
    <text x="12" y="62" font-size="5" fill="var(--brown)" font-weight="700">Increasing</text>
    <polygon points="44,58 48,52 52,58" fill="var(--brown)"/><rect x="46.5" y="58" width="3" height="6" fill="var(--brown)"/>
    <text x="12" y="68" font-size="3" fill="#777">The market is growing</text>
    <text x="12" y="72" font-size="3" fill="#777">steadily every year</text>
  </svg>
</section>

<section class="slide">
  <div class="title case">Construction Infographic</div>
  <div class="photo" style="left:6px;top:34px;width:120px;height:108px;background:linear-gradient(180deg,#f3dfa8 0%,#f4f4f4 45%,#a9cf80 100%)" role="img" aria-label="Tower crane lifting a small house"></div>
  <div class="abs" style="left:150px;top:38px;font-size:4.6px;font-weight:700;color:#333">Description</div>
  <div class="abs tiny" style="left:150px;top:44px;width:98px">For every 6 emails received, we get 1 phone calls. Suitable for all categories business and personal presentation, eaque ipsa quae ab illo.</div>
  <svg class="abs" style="left:148px;top:66px" width="104" height="70" viewBox="0 0 104 70">
    <g stroke="#e0e0e0" stroke-width=".5"><line x1="0" y1="10" x2="104" y2="10"/><line x1="0" y1="30" x2="104" y2="30"/><line x1="0" y1="50" x2="104" y2="50"/></g>
    <g fill="var(--brown)"><rect x="8" y="30" width="6" height="30"/><rect x="40" y="22" width="6" height="38"/><rect x="72" y="14" width="6" height="46"/></g>
    <g fill="var(--green)"><rect x="15" y="40" width="6" height="20"/><rect x="47" y="34" width="6" height="26"/><rect x="79" y="26" width="6" height="34"/></g>
    <g fill="var(--green-l)"><rect x="22" y="48" width="6" height="12"/><rect x="54" y="44" width="6" height="16"/><rect x="86" y="36" width="6" height="24"/></g>
    <line x1="0" y1="60" x2="104" y2="60" stroke="#999" stroke-width=".5"/>
    <g font-size="3" fill="#777" text-anchor="middle"><text x="18" y="66">Category 1</text><text x="50" y="66">Category 2</text><text x="82" y="66">Category 3</text></g>
  </svg>
</section>

</main>
</body>
</html>
```